A New Website - Harwell & Tansley Trade Council

Website Brief for Harwell and Tansley Trade Council
Overview

The chamber needs to revamp the current website that is not working.
www.harwellandtansleycouncil.example
We are looking to revamp the website and create a new professional, user-friendly, and dynamic website to showcase the chamber's services while allowing minimal day-to-day interference for the in house team.

The Chamber and members use the website for :
1. Presenting the chamber , members, activities and services to the business community.
2. The User will be able to
1. See our activities, events and register interest
2. Access membership information, benefits and register using an external link ( Pellory Mailhub )
3. Access News and reports that our team posts ( either in the website or using an external source)
4. Business will be able to access our members Directory ( in the website or outside throgh links)
5. Include a Chatterlo Chat for easy access to our team with an initial set of automated responses.

The rest of the pages will offer general information about the chamber, our structure and our services .

Target Market(s)

Corporates , Governments & Business Executives

Industry/Entity Type

Chamber of Commerce

Coding

Coded - Design and coding required

Number of Pages Required

5+ page

Font styles to use
Sans Serif
Other font styles liked:
• we are suing georgia in house for all publications

Colors
0054AA
0677BA
7BADD7
CADEEF
E8F1F8
FFF300
FFF600
FEFA6F
FFFEC7
FFFEE8
EB3D1F
EC4F4E
F09395
F8D3D4
FCEDEE

Requirements
Must have
• A clean Design, corporate , with high quality images mainly hours and a few generic ones.
Nice to have
• Responsive, user friendly quick
Should not have
• should not be busy , or chidish..

```html
<!DOCTYPE html>
<html lang="en">
<head>
<meta charset="utf-8">
<title>Harwell &amp; Tansley Trade Council</title>
<link href="https://fonts.googleapis.com/css2?family=Rethink+Sans:wght@400;500;600;700;800&display=swap" rel="stylesheet">
<style>
:root{
  --blue-deep:#0054AA;
  --blue-mid:#0677BA;
  --blue-soft:#7BADD7;
  --yellow:#FFF300;
  --red:#EB3D1F;
  --pink:#F8D3D4;
  --ink:#1d1d1f;
  --grey:#444;
  --white:#fff;
}
*{box-sizing:border-box;margin:0;padding:0}
html,body{width:1200px;height:2370px;overflow:hidden;background:var(--white)}
body{font-family:"Rethink Sans",Arial,sans-serif;color:var(--ink)}
.page{position:relative;width:1200px;height:2370px;overflow:hidden}
.abs{position:absolute}
.backdrop{position:absolute;left:0;top:0;width:1200px;height:2370px}

/* top bar */
.topbar{position:absolute;left:564px;top:18px;width:660px;height:34px;background:var(--blue-deep);border-radius:17px 0 0 17px;display:flex;align-items:center;padding-left:40px;gap:26px;color:var(--white);font-size:11px;font-weight:500}
.topbar .info{display:flex;align-items:center;gap:7px}
.social{display:flex;align-items:center;gap:10px;font-size:10px;font-weight:600}
.social .dot{width:18px;height:18px;border-radius:50%;background:var(--yellow);display:inline-block;margin-right:-5px}

/* brand */
.brand{position:absolute;left:156px;top:6px;width:112px;height:112px;border-radius:50%;background:var(--white);border:3px solid var(--blue-deep);display:flex;align-items:center;justify-content:center;text-align:center;color:var(--blue-deep);font-size:12px;font-weight:700;line-height:1.25;padding:12px}

/* nav */
.nav{position:absolute;top:75px;left:470px;font-size:11.5px;color:var(--white)}
.nav a{position:absolute;white-space:nowrap;color:var(--white);text-decoration:none}
.nav a.current{color:var(--yellow);text-decoration:underline;text-underline-offset:4px}
.btn{position:absolute;display:flex;align-items:center;justify-content:center;background:var(--red);color:var(--white);font-weight:700;font-size:11.5px;border-radius:18px;text-decoration:none}

/* hero */
.hero-title{position:absolute;left:0;width:1200px;top:212px;text-align:center;color:var(--yellow);font-size:37px;font-weight:800;letter-spacing:-0.3px}
.hero-text{position:absolute;left:0;width:1200px;top:262px;text-align:center;color:var(--white);font-size:13.5px;line-height:19px}
.dots{position:absolute;top:518px;left:566px;display:flex;gap:6px}
.dots span{width:12px;height:12px;border-radius:50%;border:1.5px solid var(--white)}
.dots span.on{border-color:var(--blue-soft);background:radial-gradient(circle,var(--blue-soft) 2px,transparent 2.5px)}

/* members strip */
.member{position:absolute;top:627px;width:162px;height:86px;border:1px solid #e2e2e2;border-radius:10px;background:var(--white);display:flex;align-items:center;justify-content:center;text-align:center;font-size:18px;font-weight:700;line-height:1.1}

/* about */
.about-title{position:absolute;left:156px;top:786px;color:var(--blue-deep);font-size:29px;font-weight:800}
.about-text{position:absolute;left:156px;width:330px;font-size:10.5px;line-height:18.8px;font-weight:500;color:var(--ink)}
.era{position:absolute;height:17px;border-radius:5px;color:var(--white);font-size:9px;display:flex;align-items:center;justify-content:center}
.timeline-line{position:absolute;left:552px;top:806px;width:1px;height:300px;background:#e3e3e3}
.events{position:absolute;left:605px;width:442px;list-style:none;font-size:9.4px;line-height:15.6px;color:var(--grey);letter-spacing:-0.05px}
.events li{position:relative;padding-left:7px;margin-bottom:6.2px}
.events li::before{content:"";position:absolute;left:0;top:6px;border-left:3px solid var(--blue-mid);border-top:2px solid transparent;border-bottom:2px solid transparent}

/* stats */
.why{position:absolute;left:158px;top:1515px;color:var(--white);font-size:28.5px;font-weight:800}
.stat-num{position:absolute;font-size:46px;font-weight:800;line-height:1;letter-spacing:-1px}
.stat-label{position:absolute;color:var(--white);font-size:12.4px;line-height:14px;font-weight:400}
.red{color:var(--red)}
.blue{color:var(--blue-mid)}

/* contact */
.touch-title{position:absolute;left:156px;top:2202px;color:var(--red);font-size:29px;font-weight:800}
.touch-line{position:absolute;left:156px;color:var(--white);font-size:12px}
.contact-line{position:absolute;left:750px;color:var(--white);font-size:10.5px}
.contact-line b{color:var(--red);font-weight:700}
</style>
</head>
<body>
<div class="page">

  <svg class="backdrop" viewBox="0 0 1200 2370">
    <defs>
      <clipPath id="heroShape"><path d="M0,0 H1200 V440 Q600,680 0,435 Z"/></clipPath>
      <clipPath id="eventShape"><path d="M0,1292 Q600,1208 1200,1290 V1762 Q620,1845 0,1755 Z"/></clipPath>
      <clipPath id="buildingShape"><path d="M0,1790 Q620,1870 1200,1775 V2370 H0 Z"/></clipPath>

      <linearGradient id="heroBase" x1="0" y1="0" x2="0" y2="1">
        <stop offset="0" stop-color="#2e2a27"/>
        <stop offset=".22" stop-color="#4a3a2b"/>
        <stop offset=".45" stop-color="#6a4a26"/>
        <stop offset=".62" stop-color="#3b2d22"/>
        <stop offset="1" stop-color="#1c1a19"/>
      </linearGradient>
      <radialGradient id="heroGlow" cx=".5" cy=".48" r=".5">
        <stop offset="0" stop-color="#8a5a2a" stop-opacity=".75"/>
        <stop offset="1" stop-color="#8a5a2a" stop-opacity="0"/>
      </radialGradient>
      <linearGradient id="heroCrowd" x1="0" y1="0" x2="0" y2="1">
        <stop offset="0" stop-color="#2a2624" stop-opacity="0"/>
        <stop offset="1" stop-color="#2a2624" stop-opacity=".85"/>
      </linearGradient>

      <linearGradient id="eventBase" x1="0" y1="0" x2="1" y2="0">
        <stop offset="0" stop-color="#3a3a42"/>
        <stop offset=".35" stop-color="#2c2c32"/>
        <stop offset=".6" stop-color="#4a4238"/>
        <stop offset="1" stop-color="#33302e"/>
      </linearGradient>
      <radialGradient id="eventLight" cx=".62" cy=".55" r=".35">
        <stop offset="0" stop-color="#6d6558" stop-opacity=".7"/>
        <stop offset="1" stop-color="#6d6558" stop-opacity="0"/>
      </radialGradient>
      <radialGradient id="eventCool" cx=".1" cy=".3" r=".3">
        <stop offset="0" stop-color="#5a6070" stop-opacity=".6"/>
        <stop offset="1" stop-color="#5a6070" stop-opacity="0"/>
      </radialGradient>

      <linearGradient id="buildingStone" x1="0" y1="0" x2="0" y2="1">
        <stop offset="0" stop-color="#8a8d88"/>
        <stop offset=".55" stop-color="#7a7a72"/>
        <stop offset=".8" stop-color="#3a3834"/>
        <stop offset="1" stop-color="#161514"/>
      </linearGradient>
      <linearGradient id="buildingTrees" x1="0" y1="0" x2="1" y2="0">
        <stop offset="0" stop-color="#2f3a2a" stop-opacity=".95"/>
        <stop offset=".3" stop-color="#3d4a34" stop-opacity="0"/>
        <stop offset=".7" stop-color="#3d4a34" stop-opacity="0"/>
        <stop offset="1" stop-color="#2f3a2a" stop-opacity=".95"/>
      </linearGradient>
      <linearGradient id="buildingShade" x1="0" y1="0" x2="0" y2="1">
        <stop offset="0" stop-color="#111" stop-opacity="0"/>
        <stop offset=".6" stop-color="#111" stop-opacity=".15"/>
        <stop offset="1" stop-color="#111" stop-opacity=".85"/>
      </linearGradient>
    </defs>

    <path d="M0,0 H1200 V450 Q600,660 0,490 Z" fill="var(--pink)"/>
    <g role="img" aria-label="Photograph of a crowded networking reception in a wood-panelled hall" clip-path="url(#heroShape)">
      <rect width="1200" height="600" fill="url(#heroBase)"/>
      <rect width="1200" height="600" fill="url(#heroGlow)"/>
      <rect y="300" width="1200" height="300" fill="url(#heroCrowd)"/>
    </g>

    <path d="M0,1292 Q560,1190 1200,1238 V1775 Q620,1870 0,1790 Z" fill="var(--pink)"/>
    <g role="img" aria-label="Photograph of members talking at a trade exhibition" clip-path="url(#eventShape)">
      <rect y="1200" width="1200" height="660" fill="url(#eventBase)"/>
      <rect y="1200" width="1200" height="660" fill="url(#eventLight)"/>
      <rect y="1200" width="1200" height="660" fill="url(#eventCool)"/>
    </g>

    <g role="img" aria-label="Photograph of the chamber's stone office building framed by trees" clip-path="url(#buildingShape)">
      <rect y="1770" width="1200" height="600" fill="url(#buildingStone)"/>
      <rect y="1770" width="1200" height="600" fill="url(#buildingTrees)"/>
      <rect y="1770" width="1200" height="600" fill="url(#buildingShade)"/>
    </g>
  </svg>

  <!-- header -->
  <div class="brand">Harwell &amp; Tansley Trade Council</div>

  <div class="topbar">
    <span class="info">
      <svg width="12" height="12" viewBox="0 0 12 12"><circle cx="6" cy="6" r="5.5" fill="#dfe6ef"/><path d="M6 3v3.2l2 1.2" stroke="#0054AA" stroke-width="1.2" fill="none"/></svg>
      Monday - Friday 09:30-17:00.
    </span>
    <span class="info">
      <svg width="12" height="12" viewBox="0 0 12 12"><path d="M2.5 1.5l2 .3.8 2.2-1.2 1a6 6 0 0 0 2.9 2.9l1-1.2 2.2.8.3 2c-4.5.6-8.6-3.5-8-8z" fill="none" stroke="#fff" stroke-width="1"/></svg>
      (+44) 020 7946 0381
    </span>
    <span class="social"><span>Friendlane</span><span class="dot"></span><span>Pinnaro</span><span>Linkrow</span><span>Clipcast</span></span>
  </div>

  <nav class="nav">
    <a class="current" style="left:0">Home</a>
    <a style="left:55px">About Us</a>
    <a style="left:125px">Networking</a>
    <a style="left:208px">Information</a>
    <a style="left:299px">Find Expertise</a>
    <a style="left:402px">Contact Us</a>
  </nav>
  <a class="btn" style="left:966px;top:67px;width:77px;height:34px">Join Us</a>

  <!-- hero -->
  <h1 class="hero-title">Get Business Support</h1>
  <p class="hero-text">Our various tiers are tailored to provide businesses of all sectors<br>and sizes the support they need.</p>
  <a class="btn" style="left:491px;top:314px;width:101px;height:33px">Get Started</a>
  <a class="btn" style="left:602px;top:314px;width:106px;height:33px">See Benefits</a>
  <div class="dots"><span></span><span></span><span class="on"></span><span></span></div>

  <!-- member strip -->
  <div class="member" style="left:-6px;color:#6f86e8">Vornel</div>
  <div class="member" style="left:169px;color:#222">Meadowlark Farms</div>
  <div class="member" style="left:344px;color:#222;font-weight:500;letter-spacing:2px;font-size:14px">OSTRIN CAPITAL</div>
  <div class="member" style="left:519px;color:#222;font-size:15px">domuslar</div>
  <div class="member" style="left:694px;color:#1a6b3c;font-weight:500;font-size:16px">Distilra Limited</div>
  <div class="member" style="left:868px;color:#e0342a;font-size:23px">Quintek</div>
  <div class="member" style="left:1043px;color:#777;font-weight:500;font-size:16px">Orlanda Café</div>

  <!-- about -->
  <h2 class="about-title">About Us</h2>
  <p class="about-text" style="top:838px">The Harwell &amp; Tansley Trade Council Stands As A Leading International Business Organisation, Uniting Members Committed To Responsible Economic And Social Development, Open Markets, And The Principles Of The Rule Of Law And Democracy.</p>
  <p class="about-text" style="top:950px">Its Membership Comprises Prominent Global Companies Across A Diverse Range Of Sectors, Including Banking And Finance, Consulting, Consumer Goods, Energy And Mining, Manufacturing, Media, Technology, And Infrastructure. Through This Broad Spectrum Of Industries, The Council Fosters A Collaborative Environment Where Leaders Work Towards Sustainable Growth And Mutual Prosperity In Both The UK, Colombia And Latin America.</p>
  <a class="btn" style="left:156px;top:1125px;width:140px;height:34px">Meet Our Members</a>

  <div class="timeline-line"></div>
  <div class="era" style="left:522px;top:789px;width:62px;background:var(--blue-mid)">1992 - 1996</div>
  <div class="era" style="left:519px;top:953px;width:68px;background:var(--blue-soft)">2002 - Today</div>

  <ul class="events" style="top:789px">
    <li>Prime Minister Sir Edmund Harlow visited Colombia</li>
    <li>President Velarde and Mr. Harlow opened negotiations for an Investment Promotion and Protection Agreement (IPPA) and Double Taxation Agreement</li>
    <li>First meeting of TFG (Trade Facilitation Group) in London in the presence of Dr. Arbeláez</li>
    <li>Arbeláez then Minister of Foreign Trade. A sub-committee was formed to actively promote trade and investment and try to set up a Chamber of Commerce</li>
    <li>H&amp;TTC was founded in 1996 with twelve companies, six Colombian and six British, who agreed to become founding sponsor members</li>
  </ul>
  <ul class="events" style="top:953px">
    <li>Business Summits with presidents of Colombia Mr. Rodrigo Salcedo (2002,2005), Tomás Arbeláez (2011), Mateo Quintana (2021)</li>
    <li>Launch of the H&amp;TTC Business &amp; Social Awards (2006)</li>
    <li>20th Anniversary with keynote speakers Former Prime Minister Edmund Harlow and Tomás Arbeláez (2016)</li>
    <li>Launch of the Colombia Investment Roadshow (2018) and series 2018- 2024. Guest Speaker : President of Colombia Mr Mateo Quintana and Key government Officials</li>
    <li>Re -Launch of the Responsible Business Awards (2020): Guest Judges" Civic Trade Compact, RRI, Fair Capital Principles</li>
    <li>Re -Launch of the Annual Conference (2024) -Key Note Speaker: Lord Anthony Greaves of Ashcombe.</li>
  </ul>

  <!-- why join -->
  <h2 class="why">Why Join Us</h2>

  <svg class="abs" style="left:469px;top:1417px" width="66" height="66" viewBox="0 0 66 66" fill="none" stroke="#fff" stroke-width="2">
    <rect x="8" y="3" width="42" height="54" rx="3"/>
    <rect x="12" y="8" width="34" height="10" fill="var(--red)" stroke="none"/>
    <path d="M14 26h24M14 33h20M14 40h16"/>
    <circle cx="52" cy="38" r="8" fill="var(--red)"/>
    <path d="M47 45l-2 12 7-4 7 4-2-12"/>
  </svg>
  <div class="stat-num red" style="left:552px;top:1419px">30</div>
  <div class="stat-label" style="left:552px;top:1461px">Years of trade &amp; Investment<br>support experience</div>

  <svg class="abs" style="left:791px;top:1417px" width="76" height="70" viewBox="0 0 76 70" fill="none" stroke="#fff" stroke-width="2">
    <circle cx="20" cy="32" r="15"/>
    <circle cx="56" cy="32" r="15"/>
    <circle cx="38" cy="22" r="17" fill="var(--blue-mid)" stroke="none"/>
    <path d="M38 13l3 6 6 1-4.5 4 1 6-5.5-3-5.5 3 1-6-4.5-4 6-1z"/>
    <path d="M20 47l-3 18M56 47l3 18M38 39v26"/>
  </svg>
  <div class="stat-num blue" style="left:880px;top:1419px">+500</div>
  <div class="stat-label" style="left:880px;top:1465px">High Profile Events</div>

  <svg class="abs" style="left:469px;top:1575px" width="56" height="68" viewBox="0 0 56 68" fill="none" stroke="#fff" stroke-width="2">
    <rect x="4" y="2" width="46" height="64" rx="3"/>
    <path d="M10 2v64M50 12h4M50 24h4M50 36h4"/>
    <path d="M24 14l5 1 2 5-3 2a13 13 0 0 0 6 6l2-3 5 2 1 5c-10 1-19-8-18-18z" stroke="var(--blue-mid)" stroke-width="3"/>
    <rect x="20" y="50" width="20" height="7"/>
  </svg>
  <div class="stat-num blue" style="left:552px;top:1573px">+17k</div>
  <div class="stat-label" style="left:552px;top:1613px">High profile business and<br>government contacts</div>

  <svg class="abs" style="left:791px;top:1575px" width="76" height="70" viewBox="0 0 76 70" fill="none" stroke="#fff" stroke-width="2">
    <path d="M8 36l34-26 10 36-34-4z"/>
    <path d="M8 36l5 10"/>
    <path d="M20 42l10 22h8l-6-20" fill="var(--red)" stroke="var(--red)"/>
    <path d="M56 10l8-6M60 22h10M58 34l8 4"/>
  </svg>
  <div class="stat-num red" style="left:880px;top:1573px">+25</div>
  <div class="stat-label" style="left:880px;top:1615px">Missions and Market visits<br>+25 organised</div>

  <!-- contact -->
  <h2 class="touch-title">Get in touch</h2>
  <p class="touch-line" style="top:2261px;font-weight:500">Visituson Tuesdays - Open House</p>
  <p class="touch-line" style="top:2282px;color:var(--red);font-size:13.5px">Business Lounge , Meeting rooms , Conference Venue , Free Coffee</p>
  <p class="touch-line" style="top:2304px;font-size:13.5px">14 Kelworth Avenue , London WC9 4QX</p>

  <p class="contact-line" style="top:2263px"><b>Phone:</b> +44 ( 0 ) 20 7946 0382</p>
  <p class="contact-line" style="top:2284px"><b>Email:</b> info@harwellandtansleycouncil.example</p>
  <div class="social abs" style="left:750px;top:2310px;color:var(--white)"><span>Friendlane</span><span class="dot"></span><span>Pinnaro</span><span>Linkrow</span><span>Clipcast</span></div>

</div>
</body>
</html>
```